Pembrook Nightclub Flyer Grand Opening

Grand Opening Teaser Flyer For Nightclub

Text for flyer:
PEMBROOK
Nightclub + Lounge
Opening Fall 2018
Downtown Sacramento
Now Hiring (All Positions)
www.pembrookvenue.example
Powered by HALM Acoustics

Email Resume to: club@pembrookvenue.example

Target Market(s)

Upscale Nightclub and Lounge

Industry/Entity Type

Night Club

Font styles to use
Sans Serif

Colors
9ccb3b
0393ce
0355a3
b2b2b2
000000

Requirements
Must have
• Vibrant colors like the flyer example, and our logo. For use on Facebook and Instagram, will be boosted as well.
Nice to have
• Something artsy like the flyer example but not required

```html
<!DOCTYPE html>
<html lang="en">
<head>
<meta charset="utf-8">
<title>Pembrook Nightclub + Lounge — Opening Fall 2018</title>
<link rel="stylesheet" href="https://fonts.googleapis.com/css2?family=Lato:wght@400&family=Yellowtail&display=swap">
<style>
  :root {
    --ink: #000000;
    --white: #ffffff;
    --lime: #9ccb3b;
    --cyan: #0393ce;
    --cyan-bright: #1fb8f0;
    --navy: #0355a3;
    --grey: #b2b2b2;
    --amber: #e8b13a;
    --teal: #1fa6a0;
  }
  html, body {
    margin: 0;
    padding: 0;
    width: 1200px;
    height: 629px;
    overflow: hidden;
    background: var(--ink);
  }
  .flyer {
    position: relative;
    width: 1200px;
    height: 629px;
    overflow: hidden;
    font-family: "Lato", "Helvetica Neue", Arial, sans-serif;
    color: var(--white);
  }
  .scene {
    position: absolute;
    inset: 0;
    background:
      radial-gradient(ellipse 260px 150px at 1010px 70px, rgba(240,190,60,0.85), transparent 70%),
      radial-gradient(ellipse 240px 140px at 830px 150px, rgba(230,140,50,0.7), transparent 70%),
      radial-gradient(ellipse 300px 160px at 620px 90px, rgba(40,190,170,0.8), transparent 70%),
      radial-gradient(ellipse 260px 150px at 430px 150px, rgba(30,120,200,0.75), transparent 70%),
      radial-gradient(ellipse 200px 120px at 1130px 210px, rgba(200,170,70,0.6), transparent 70%),
      radial-gradient(ellipse 140px 60px at 790px 200px, rgba(220,90,40,0.7), transparent 70%),
      radial-gradient(ellipse 520px 120px at 980px 430px, rgba(40,170,200,0.7), transparent 70%),
      radial-gradient(ellipse 360px 110px at 1040px 540px, rgba(200,190,80,0.45), transparent 70%),
      radial-gradient(ellipse 420px 90px at 880px 340px, rgba(3,147,206,0.65), transparent 70%),
      linear-gradient(180deg, #0b2a45 0%, #103a4a 30%, #061420 46%, #0a2f45 62%, #06324a 80%, #041622 100%);
  }
  .scene-skyline {
    position: absolute;
    left: 0;
    right: 0;
    top: 210px;
    height: 110px;
    background: linear-gradient(180deg, rgba(5,12,22,0) 0%, rgba(5,12,22,0.85) 45%, rgba(5,12,22,0.6) 100%);
  }
  .scene-shade {
    position: absolute;
    inset: 0;
    background: linear-gradient(90deg, rgba(0,0,0,0.85) 0%, rgba(0,0,0,0.55) 28%, rgba(0,0,0,0) 55%);
  }
  .brand-badge {
    position: absolute;
    left: 43px;
    top: 28px;
    width: 286px;
    height: 286px;
    border-radius: 50%;
    background: var(--ink);
    border: 6px solid var(--cyan-bright);
    box-sizing: border-box;
    display: flex;
    align-items: center;
    justify-content: center;
  }
  .brand-name {
    font-size: 32px;
    letter-spacing: 6px;
    color: var(--white);
    padding-left: 6px;
  }
  .tagline {
    position: absolute;
    left: 37px;
    top: 340px;
    margin: 0;
    font-size: 28px;
    line-height: 34px;
    font-weight: 400;
    color: var(--lime);
  }
  .opening {
    position: absolute;
    left: 400px;
    top: 352px;
    margin: 0;
    font-family: "Yellowtail", "Brush Script MT", cursive;
    font-weight: 400;
    font-size: 62px;
    line-height: 70px;
    color: var(--white);
    transform: rotate(-4deg);
    transform-origin: left center;
    white-space: nowrap;
  }
  .opening-year { color: var(--cyan-bright); }
  .detail {
    position: absolute;
    left: 22px;
    margin: 0;
    white-space: nowrap;
    font-weight: 400;
  }
  .detail-city   { top: 416px; font-size: 27px; line-height: 34px; }
  .detail-hiring { top: 462px; font-size: 25px; line-height: 32px; }
  .detail-sound  { top: 503px; font-size: 23px; line-height: 32px; }
  .detail-email  { top: 547px; font-size: 18px; line-height: 24px; }
  .detail-web    { top: 586px; font-size: 23px; line-height: 28px; }
</style>
</head>
<body>
  <main class="flyer">
    <div class="scene" role="img" aria-label="Night city river scene with a lit clock tower and stone bridge under a vivid teal, blue and amber starry nebula sky, reflected in the water"></div>
    <div class="scene-skyline"></div>
    <div class="scene-shade"></div>

    <div class="brand-badge">
      <span class="brand-name">PEMBROOK</span>
    </div>

    <h2 class="tagline">Nightclub + Lounge</h2>

    <h1 class="opening">Opening Fall <span class="opening-year">2018</span></h1>

    <p class="detail detail-city">Downtown Sacramento</p>
    <p class="detail detail-hiring">Now Hiring (All Positions)</p>
    <p class="detail detail-sound">Powered by HALM Acoustics</p>
    <p class="detail detail-email">Email Resume to: club@pembrookvenue.example</p>
    <p class="detail detail-web">www.pembrookvenue.example</p>
  </main>
</body>
</html>
```